Pin Oak Media Outdoor Advertising Corporate Stationery Design

We need a full corporate stationary design for our company Pin Oak Media. We setup and lease billboards, building wraps, trailer ads and construction hoardings.

We need to establish our branding and our newly created logo. All our brand identity should point towards our values, vision and mission.

We are open to fresh new ideas for our stationary design as long as it ultimately reflects the brand & logo.

Corporate Stationary List:
1. Business Card Design
2. Letterhead Design
3. Email Signature Design
4. “Advertise Here” Design (for placement on empty billboards, etc)

All designs must include our logo and be kept simple, modern, friendly and effective.

All designs should please be provided in Illustrator, Photoshop and InDesign file formats.

More details are attached in Word.

Hey

The project has been guaranteed. We like what has been submitted so far but we''d like to see a few concepts for the "Advertise Here" design for open billboards please.

Thanks!

Target Market(s)

Male and female, corporates, business owners, media buying agencies, government & all age groups.

Industry/Entity Type

Construction

Requirements
Must have
• All designs must incorporate our colours: Pantone 319C, 320C, 321C & Hexachrome Black C.

1.Business Card Design
a. Logo
b. Name
c. Mobile
d. Landline
e. Website
f. Facebook
g. Twitter
2. Letterhead Design
a. Logo
b. Mobile
c. Landline
d. Website
e. CC reg number
f. BEE level 4 contributor
g. PRTVA member
h. Postal Address
3. Email Signature Design
a. Logo
b. Name
c. Mobile
d. Landline
e. BEE level 4 contributor
f. PRTVA member
g. Website
h. Facebook
i. Twitter
4. “Advertise Here” Design (for placement on empty billboards, etc) Majority ratio of 2:1 (eg 6m wide by 3m high) - Please use 2 attached photos.
a. Logo .co.za
b. Contact Mirela
c. Mobile
Nice to have
• Come up with a cool slogan / tagline for Business Cards, “Advertise Here” Design

```html
<!DOCTYPE html>
<html lang="en">
<head>
<meta charset="utf-8">
<title>Pin Oak Media – Business Card</title>
<link rel="stylesheet" href="https://fonts.googleapis.com/css2?family=Mulish:wght@400;600;800&display=swap">
<style>
  :root {
    --stage: #eeeeec;
    --card-white: #ffffff;
    --card-black: #000000;
    --stripe-grey: #9a9a9a;
    --brand-teal: #1aa3ad;
    --text-light: #ffffff;
    --text-dark: #111111;
  }
  html, body {
    margin: 0;
    padding: 0;
    width: 1200px;
    height: 466px;
    overflow: hidden;
    background: var(--stage);
  }
  .stationery {
    position: relative;
    width: 1200px;
    height: 466px;
  }
  .card {
    position: absolute;
    top: 77px;
    width: 542px;
    height: 310px;
    box-shadow: 0 3px 8px rgba(0,0,0,0.25);
  }
  .card--front { left: 26px; }
  .card--back  { left: 633px; }
  .card svg { display: block; }
  .card-white  { fill: var(--card-white); }
  .card-black  { fill: var(--card-black); }
  .card-stripe { fill: var(--stripe-grey); }
  .tagline {
    font-family: "Mulish", sans-serif;
    font-weight: 800;
    font-size: 17px;
    fill: var(--text-dark);
    letter-spacing: 0.5px;
  }
  .brand-name {
    font-family: "Mulish", sans-serif;
    font-weight: 600;
    fill: var(--brand-teal);
  }
  .brand-dot { fill: var(--brand-teal); }
  .holder-name {
    font-family: "Mulish", sans-serif;
    font-weight: 400;
    font-size: 22px;
    fill: var(--text-light);
  }
  .holder-title { font-size: 13px; }
  .contact-line {
    font-family: "Mulish", sans-serif;
    font-weight: 400;
    font-size: 12.5px;
    fill: var(--text-light);
  }
  .website-line {
    font-family: "Mulish", sans-serif;
    font-weight: 400;
    font-size: 14px;
    letter-spacing: 2px;
    fill: var(--text-light);
  }
  .icon-stroke { fill: none; stroke: var(--text-light); stroke-width: 1; }
  .icon-fill { fill: var(--text-light); }
  .icon-social { fill: var(--brand-teal); }
</style>
</head>
<body>
<main class="stationery">

  <!-- Front of the business card -->
  <section class="card card--front" aria-label="Business card front">
    <svg viewBox="0 0 525 300" width="542" height="310">
      <rect class="card-white" x="0" y="0" width="525" height="300"/>
      <polygon class="card-stripe" points="350,0 360,0 75,300 65,300"/>
      <polygon class="card-black" points="360,0 525,0 525,300 75,300"/>

      <circle class="brand-dot" cx="78" cy="92" r="30"/>
      <text class="brand-name" font-size="26" text-anchor="middle"
            transform="translate(165,128) rotate(-46.5)">Pin Oak Media</text>

      <text class="tagline" text-anchor="middle"
            transform="translate(250,97) rotate(-46.5)">Advertise Here</text>

      <text class="holder-name" x="312" y="124">YOUR NAME <tspan class="holder-title">/ Title</tspan></text>

      <g class="contact-block" text-anchor="end">
        <text class="contact-line" x="483" y="195">+27 21 555 0148</text>
        <text class="contact-line" x="483" y="213">+27 82 555 0148</text>
        <text class="contact-line" x="483" y="231">www.pinoakmedia.co.za</text>
        <text class="contact-line" x="483" y="249">pinoakmedia.co.za</text>
        <text class="contact-line" x="483" y="267">pinoakmedia.co.za</text>
      </g>

      <g class="contact-icons">
        <!-- landline -->
        <circle class="icon-stroke" cx="494" cy="191" r="4.5"/>
        <path class="icon-fill" d="M491.5 189.5 l1.5 -1 l1 2 l-1 0.8 l1.5 1.7 l0.9 -0.9 l1.8 1.2 l-1 1.4 c-2 0 -4.7 -2.8 -4.7 -5.2z"/>
        <!-- mobile -->
        <rect class="icon-stroke" x="491" y="204" width="6" height="10" rx="1"/>
        <rect class="icon-fill" x="492.5" y="206" width="3" height="4.5"/>
        <!-- website -->
        <circle class="icon-stroke" cx="494" cy="227" r="4.5"/>
        <ellipse class="icon-stroke" cx="494" cy="227" rx="2" ry="4.5"/>
        <line class="icon-stroke" x1="489.5" y1="227" x2="498.5" y2="227"/>
        <!-- social pages -->
        <rect class="icon-social" x="489.5" y="240.5" width="9" height="9"/>
        <rect class="icon-social" x="489.5" y="258.5" width="9" height="9"/>
      </g>
    </svg>
  </section>

  <!-- Back of the business card -->
  <section class="card card--back" aria-label="Business card back">
    <svg viewBox="0 0 525 300" width="542" height="310">
      <rect class="card-white" x="0" y="0" width="525" height="300"/>
      <polygon class="card-stripe" points="350,0 360,0 75,300 65,300"/>
      <polygon class="card-black" points="360,0 525,0 525,300 75,300"/>

      <circle class="brand-dot" cx="95" cy="75" r="30"/>
      <text class="brand-name" font-size="22" x="40" y="142">Pin Oak Media</text>

      <text class="tagline" text-anchor="middle"
            transform="translate(250,97) rotate(-46.5)">Advertise Here</text>

      <text class="website-line" x="483" y="185" text-anchor="end">www.pinoakmedia.co.za</text>
    </svg>
  </section>

</main>
</body>
</html>
```